Fahrzeugbeschriftung für einen Elektriker
Zielgruppe
ich bin ein Elektriker im Handwerk ich installiere Häuser Industrieanlagen. und baue Schaltschränke.
ich baue auch Lampen und verkaufe diese, jedoch will ich den Bereich leuchten bau nicht als Werbung auf meinem Auto haben es soll Klar die Elektro Installation im Vordergrund stehen, da ich über sie mein Geld verdiene.
Ich habe bereits ein logo, sende ich mit.
ich habe auch eine Vorstellung von einem Design jedoch bin ich auch für etwas komplett anderes offen.
Ich habe auch mal ein par Bilder, von leuchten oder Schaltschränken die ich Baue mit gesendet.
Zu meiner Vorstellung:
ich habe Ein Bild mit gesendet, von einem goldenen Barkel Tarsa e, da wo Tarsa e steht, hätte ich gerne mein Logo
und vielleicht ein paar linien in matt schwarz vielleicht mit Steckern an den enden.
Jedoch wie gesagt wenn ein designe was nicht meiner Vorstellung entspricht mich umhaut, bin ich auch dafür zu haben.
den Slogan werde ich noch nachreichen.
Fahrzeug Daten:
Hersteller/Marke Barkel Tarsa
Tarsa Lastro-e L (QW58B), Elektro
HSN 4127
TSN QRT
Daten was ich anbiete:
Elektroinstallation
Verteilerbau
Netzwerk und Industrie Service
Photovoltaikanlagen
Lichtplanung
was noch drauf muss
Kontaktdaten
Fon: 0152 / 87 41 90 16
www.elektrikerfunkenwerk.de
tobiaskern@elektrikerfunkenwerk.de
Instagram: elektriker_funkenwerk
Tobias Kern
77812Ortenhof Mühlgasse 9
Viel Spaß Gruß Das Funkenwerk
Aufgabenstellung
ich möchte Einen wieder Erkennungswert für mein Auto es muss jedem sofort ins Auge springen jedoch auch nicht überladen wirken. ich habe ein Designvorstellung.

```html
<!DOCTYPE html>
<html lang="de">
<head>
<meta charset="utf-8">
<title>Funkenwerk – Fahrzeugbeschriftung</title>
<link href="https://fonts.googleapis.com/css2?family=Montserrat:wght@700&family=Roboto+Condensed:wght@400;700&display=swap" rel="stylesheet">
<style>
  :root {
    --wrap-yellow: #f4c300;
    --logo-grey: #3b3b3b;
    --ink: #111111;
    --cable-black: #141414;
  }
  html, body {
    margin: 0;
    padding: 0;
    width: 1200px;
    height: 675px;
    overflow: hidden;
  }
  .wrap-panel {
    position: relative;
    width: 1200px;
    height: 675px;
    overflow: hidden;
    background: var(--wrap-yellow);
    font-family: "Roboto Condensed", sans-serif;
    color: var(--ink);
  }
  .brand {
    position: absolute;
    left: 380px;
    top: 80px;
    transform: rotate(-2.5deg);
    transform-origin: left bottom;
  }
  .brand-name {
    margin: 0;
    font-family: "Montserrat", sans-serif;
    font-weight: 700;
    font-size: 80px;
    line-height: 1;
    letter-spacing: 1px;
    color: var(--logo-grey);
    white-space: nowrap;
  }
  .brand-tagline {
    margin: 8px 0 0 100px;
    font-family: "Montserrat", sans-serif;
    font-weight: 700;
    font-size: 27px;
    line-height: 1;
    color: var(--logo-grey);
    white-space: nowrap;
  }
  .services {
    position: absolute;
    left: 480px;
    top: 258px;
    margin: 0;
    font-weight: 700;
    font-size: 19px;
    line-height: 1.25;
    white-space: nowrap;
    transform: rotate(-2.5deg);
    transform-origin: left top;
  }
  .services span { display: block; }
  .contact {
    position: absolute;
    left: 70px;
    top: 355px;
    margin: 0;
    padding: 0;
    list-style: none;
    font-size: 16px;
    line-height: 1.25;
    white-space: nowrap;
    transform: rotate(-2deg);
    transform-origin: left top;
  }
  .contact li {
    display: flex;
    align-items: flex-start;
    gap: 8px;
    margin-bottom: 4px;
  }
  .contact-icon {
    flex: none;
    width: 14px;
    height: 14px;
    margin-top: 2px;
  }
  .cable-art {
    position: absolute;
    left: 400px;
    top: 345px;
    width: 520px;
    height: 220px;
    border-radius: 40px;
    background: linear-gradient(90deg, rgba(20,20,20,0.85), rgba(20,20,20,0.95));
  }
</style>
</head>
<body>
<main class="wrap-panel">

  <header class="brand">
    <h1 class="brand-name">FUNKENWERK</h1>
    <p class="brand-tagline">ELEKTROFACHBETRIEB TOBIAS KERN</p>
  </header>

  <p class="services">
    <span>Elektroinstallation - Verteilerbau&nbsp; - Netzwerk und Industrie Service</span>
    <span>Photovoltaikanlagen&nbsp; - Lichtplanung</span>
  </p>

  <ul class="contact">
    <li>
      <svg class="contact-icon" viewBox="0 0 16 16" aria-hidden="true">
        <path d="M8 1a5 5 0 0 0-5 5c0 4 5 9 5 9s5-5 5-9a5 5 0 0 0-5-5z" fill="var(--ink)"/>
        <circle cx="8" cy="6" r="2" fill="var(--wrap-yellow)"/>
      </svg>
      <span>Tobias Kern<br>77812 Ortenhof Mühlgasse 9</span>
    </li>
    <li>
      <svg class="contact-icon" viewBox="0 0 16 16" aria-hidden="true">
        <circle cx="8" cy="8" r="7.5" fill="var(--ink)"/>
        <path d="M5 4.5l1.6-.5 1 2.2-1 .8a5 5 0 0 0 2.4 2.4l.8-1 2.2 1-.5 1.6C8.5 11.5 4.5 7.5 5 4.5z" fill="var(--wrap-yellow)"/>
      </svg>
      <span>0152 / 87 41 90 16</span>
    </li>
    <li>
      <svg class="contact-icon" viewBox="0 0 16 16" aria-hidden="true">
        <circle cx="8" cy="8" r="7.5" fill="var(--ink)"/>
        <circle cx="8" cy="8" r="4.5" fill="none" stroke="var(--wrap-yellow)" stroke-width="1"/>
        <path d="M3.5 8h9M8 3.5v9" stroke="var(--wrap-yellow)" stroke-width="1"/>
      </svg>
      <span>www.elektrikerfunkenwerk.de</span>
    </li>
    <li>
      <svg class="contact-icon" viewBox="0 0 16 16" aria-hidden="true">
        <circle cx="8" cy="8" r="7.5" fill="var(--ink)"/>
        <rect x="4" y="5" width="8" height="6" fill="none" stroke="var(--wrap-yellow)" stroke-width="1"/>
        <path d="M4 5l4 3.5L12 5" fill="none" stroke="var(--wrap-yellow)" stroke-width="1"/>
      </svg>
      <span>tobiaskern@elektrikerfunkenwerk.de</span>
    </li>
    <li>
      <svg class="contact-icon" viewBox="0 0 16 16" aria-hidden="true">
        <rect x="1" y="1" width="14" height="14" fill="var(--ink)"/>
      </svg>
      <span>elektriker_funkenwerk</span>
    </li>
  </ul>

  <div class="cable-art" role="img" aria-label="Matt schwarzes, gewelltes Elektrokabel mit abisolierten Adern und Funken am Ende"></div>

</main>
</body>
</html>
```